Concierge Healthcare Business Card Design and Logo

We need a logo and business card design for a new company called "Sound Haven". We will provide concierge audiological care, hearing aids, hearing exams, custom hearing protection etc to patients in the comfort of their homes and offices. We would like a sleek and modern design preferably with an Ear related logo.

Target Market(s)

People with hearing loss, Hunters, Musicians
My usual clientele are older individuals so usually 50+ years old

Industry/Entity Type

Health Care

Contact Information for Business Card

Celia Dunford, AuD
Audiologist
512-648-2917
soundhaven@mailvale.com
www.soundhaven-example.com

Logo Text

Sound Haven

Number of Pages Required

3 page

```html
<!DOCTYPE html>
<html lang="en">
<head>
<meta charset="utf-8">
<title>Sound Haven — Business Card</title>
<link rel="stylesheet" href="https://fonts.googleapis.com/css2?family=Josefin+Slab:ital,wght@0,400;0,600;1,400&display=swap">
<style>
  :root {
    --card-dark: #221f20;
    --brand-blue: #29a8e0;
    --brand-blue-soft: rgba(41, 168, 224, 0.55);
    --text-light: #ecebea;
    --backdrop: #d9d9d7;
  }
  * { margin: 0; padding: 0; box-sizing: border-box; }
  html, body {
    width: 1200px; height: 900px; overflow: hidden;
    background: var(--backdrop);
    font-family: "Josefin Slab", Georgia, serif;
  }
  .canvas { position: relative; width: 1200px; height: 900px; }
  .card {
    position: absolute; left: 285px;
    width: 630px; height: 360px;
    background: var(--card-dark);
    overflow: hidden;
    box-shadow: 0 8px 24px rgba(0,0,0,0.25);
  }
  .card--front { top: 50px; }
  .card--back { top: 470px; }

  .brand {
    display: flex; align-items: center; gap: 12px;
    color: var(--brand-blue); font-weight: 400;
  }
  .brand__dot { border-radius: 50%; background: var(--brand-blue); }
  .card--front .brand {
    position: absolute; left: 0; right: 0; top: 150px;
    justify-content: center; font-size: 46px; letter-spacing: 1px;
  }
  .card--front .brand__dot { width: 34px; height: 34px; }

  .card--back .brand {
    position: absolute; left: 40px; top: 88px;
    font-size: 26px; letter-spacing: 0.5px;
  }
  .card--back .brand__dot { width: 20px; height: 20px; }

  .decor-area {
    position: absolute; top: 0; right: 0;
    width: 210px; height: 360px;
    background: linear-gradient(200deg, var(--brand-blue) 0%, var(--brand-blue-soft) 45%, var(--card-dark) 100%);
  }

  .person { position: absolute; left: 50px; top: 160px; }
  .person__name { color: var(--brand-blue); font-size: 28px; font-weight: 400; line-height: 1; }
  .person__role { color: var(--text-light); font-size: 17px; font-style: italic; margin-top: 2px; }
  .divider {
    position: absolute; left: 44px; top: 210px;
    width: 362px; height: 1.5px; background: var(--brand-blue);
  }
  .contact { position: absolute; left: 50px; top: 228px; list-style: none; }
  .contact__item {
    display: flex; align-items: center; gap: 10px;
    color: var(--text-light); font-size: 19px; height: 32px;
  }
  .contact__icon { width: 18px; height: 18px; flex: none; }
  .contact__icon * { stroke: var(--brand-blue); fill: none; stroke-width: 1.6; }
  .web-domain { color: var(--brand-blue); }
</style>
</head>
<body>
<main class="canvas">
  <section class="card card--front" aria-label="Card front">
    <div class="brand"><span class="brand__dot"></span><span class="brand__name">Sound Haven</span></div>
  </section>

  <section class="card card--back" aria-label="Card back">
    <div class="decor-area" role="img" aria-label="Decorative blue swoosh graphic along the right edge"></div>

    <div class="brand"><span class="brand__dot"></span><span class="brand__name">Sound Haven</span></div>

    <div class="person">
      <h1 class="person__name">Celia Dunford, AuD</h1>
      <p class="person__role">Audiologist</p>
    </div>
    <div class="divider"></div>

    <ul class="contact">
      <li class="contact__item">
        <svg class="contact__icon" viewBox="0 0 20 20" aria-hidden="true"><rect x="2" y="4.5" width="16" height="11"/><path d="M2 4.5 L10 11 L18 4.5"/></svg>
        soundhaven@mailvale.com
      </li>
      <li class="contact__item">
        <svg class="contact__icon" viewBox="0 0 20 20" aria-hidden="true"><circle cx="10" cy="10" r="8.5"/><path d="M7 5.5 C6 8 8 12.5 12.5 14.5 L14 13 L12.5 11.5 L11.2 12.2 C9.8 11.3 8.8 10.2 8.2 8.8 L9 7.6 L7.8 5.2 Z"/></svg>
        512-648-2917
      </li>
      <li class="contact__item">
        <svg class="contact__icon" viewBox="0 0 20 20" aria-hidden="true"><circle cx="10" cy="10" r="8.5"/><ellipse cx="10" cy="10" rx="3.8" ry="8.5"/><path d="M1.5 10 H18.5 M3 5.5 H17 M3 14.5 H17"/></svg>
        <span>www.<span class="web-domain">soundhaven-example</span>.com</span>
      </li>
    </ul>
  </section>
</main>
</body>
</html>
```